Carrier needs an Amazing Flyer

Our business is needing a corporate flyer. At the moment we transport different products, some of them clasified as hazardous, through out center and south Peru-South America. We would like the flyer to comunicate punctuality, safety and profesionalism. Our corporate colors are green (C=85,M=25,Y=55,K=10) and black. At the moment, we are developing what the flyer should say (we will upload it later), but the flyer should have 04 parts: Clients, Vehicles, Services and Routes.

The information to every part is the following:

Clients: the ones listed in our webpage (www.cargavelorumbo.pe), which you can find in the option "Clientes". We add the text of this part in uploaded files with a .doc extension.

Vehicles: the ones listed in our webpage (www.cargavelorumbo.pe), which you can find in the option "Flota". We add the text of this part in uploaded files with a .doc extension.

Services: the ones listed in our webpage (www.cargavelorumbo.pe), which you can find in the option "Servicios". We add the text of this part in uploaded files with a .doc extension. The smart art is only a example. We would like too see more ideas but use the smart art as an example.

Routes: At the moment we are covering all South of Peru and his capital city, Lima. Thefore, we are transporting between cities around the mentioned area. An idea to show this can be a map of those Peru areas. We will like to receive more ideas about this. In order to help you draw the map, the cities adn towns that we most cover are: Lima, Pisco, Ica, Nasca, Chala, Atico, OcoƱa, Camana, Pedregal, Majes, Mollendo, Matarani, Ilo, Moquegua, Cocachacra, Tacna, Arequipa, Juliaca, Puno, Ilave, Desaguadero, Cusco, Sicuani, Chivay, Imata, Santa Lucia, Ayaviri, Puerto Maldonado, Macusani, Mazuco, Espinar. You can use google maps, to have an idea of where these cities and towns are. Any question just write us a message.

Target Market(s)

Other Business

Industry/Entity Type

Business

Requirements
Must have
• We are willing to print the flyer in a A4 format and bent it in two. Also, we will use the flyer as a digital presentation to send it to our clients by email. All the text in the flyer must be in spanish. For those who do not know the language, we will guide you. We don't want to many words in the flyer.
Nice to have
• We would like to see something that captures the attention of the reader, so he or she give it some minutes to check it out. Therefore, the parts should be strategically located.
Should not have
• Don't put in a map of South America. We are not transporting outside of Peru at the moment. This might give a wrong impression to new customers.

```html
<!DOCTYPE html>
<html lang="es">
<head>
<meta charset="utf-8">
<title>Transportes Cargavelo AQP</title>
<link rel="stylesheet" href="https://fonts.googleapis.com/css2?family=Montserrat:wght@700;800&family=Arimo:wght@400&display=swap">
<style>
  :root{
    --teal:#138a78;
    --teal-dark:#0f7565;
    --ink:#1c1c1c;
    --body:#333333;
    --tile:#e4e4e4;
    --line:#b5b5b5;
    --white:#ffffff;
  }
  *{margin:0;padding:0;box-sizing:border-box}
  html,body{width:849px;height:1200px;overflow:hidden;background:var(--white)}
  .flyer{position:relative;width:849px;height:1200px;overflow:hidden;background:var(--white);font-family:"Arimo",Arial,sans-serif;color:var(--body)}
  .brand{position:absolute;left:0;top:0;width:426px;height:103px;background:var(--white);display:flex;align-items:center;padding-left:30px;gap:14px}
  .brand-mark{width:64px;height:64px;border-radius:50%;background:var(--teal);flex:none}
  .brand-name{font-family:"Montserrat",Arial,sans-serif;font-weight:800;color:var(--ink);line-height:1}
  .brand-name .small{display:block;font-size:17px;margin-bottom:4px}
  .brand-name .big{display:block;font-size:33px;letter-spacing:-.5px}
  .web{position:absolute;left:426px;top:0;width:423px;height:103px;background:var(--teal);color:var(--white);font-family:"Arimo",Arial,sans-serif;font-size:21px;display:flex;align-items:center;justify-content:center}
  .hero{position:absolute;left:0;top:103px;width:849px;height:540px;background:linear-gradient(180deg,#6f8fb8 0%,#a9b9c6 18%,#8a7060 34%,#b9653e 52%,#a56a4a 70%,#c08d6a 100%)}
  .hero-truck{position:absolute;left:420px;top:12px;width:300px;height:290px;background:linear-gradient(180deg,#f2f2f0,#d6d8d8);border-radius:18px 40px 8px 8px}
  .hero-trailer{position:absolute;left:75px;top:145px;width:345px;height:90px;background:linear-gradient(180deg,#1d7b6a,#1a2a28)}
  .curve{position:absolute;left:0;top:0}
  .photo-disc{position:absolute;border-radius:50%;border:9px solid var(--teal);background:var(--white);overflow:hidden}
  .photo-disc span{display:block;width:100%;height:100%}
  .disc-team{left:223px;top:336px;width:190px;height:190px}
  .disc-team span{background:linear-gradient(180deg,#7fa9d8 0%,#c9c3b9 40%,#b1472d 60%,#c2b39a 100%)}
  .disc-dump{left:457px;top:407px;width:168px;height:168px}
  .disc-dump span{background:linear-gradient(180deg,#8db5e0 0%,#c7c1b4 35%,#2a8f86 60%,#c7a98a 100%)}
  .disc-tipper{left:654px;top:481px;width:164px;height:164px}
  .disc-tipper span{background:linear-gradient(180deg,#9fc2e6 0%,#4fa05a 40%,#e8e8e8 65%,#b49d80 100%)}
  .heading{font-family:"Montserrat",Arial,sans-serif;font-weight:800;letter-spacing:.5px}
  .clientes{position:absolute;left:36px;top:545px;width:370px}
  .clientes .heading{color:var(--teal);font-size:27px;margin-bottom:6px}
  .copy{font-size:13.2px;line-height:17px}
  .panel{position:absolute;left:34px;width:372px;height:165px;background:var(--teal);color:var(--white);padding:12px 18px 0 20px}
  .panel .heading{font-size:29px;margin-bottom:4px}
  .flota{top:783px}
  .servicios{top:977px}
  .routes-title{position:absolute;left:437px;top:618px;color:var(--teal);font-size:29px}
  .routes-lines{position:absolute;left:0;top:0}
  .stop{position:absolute;width:90px;height:47px;background:var(--tile);color:var(--ink);font-size:13.5px;display:flex;align-items:center;justify-content:center;text-align:center;line-height:1.05;letter-spacing:-.2px}
  .stop.tight{font-size:11.5px;letter-spacing:-.4px}
  .c1{left:436px}.c2{left:533px}.c3{left:629px}.c4{left:725px}
  .b1{left:484px}.b2{left:581px}.b3{left:677px}
  .r1{top:672px}.r2{top:729px}.r3{top:793px}.r4{top:850px}.r5{top:914px}.r6{top:971px}.r7{top:1036px}.r8{top:1092px}
  .footer-band{position:absolute;left:0;top:1180px;width:849px;height:20px;background:#000}
</style>
</head>
<body>
<div class="flyer">
  <header>
    <div class="brand">
      <div class="brand-mark"></div>
      <div class="brand-name"><span class="small">Transportes</span><span class="big">CARGAVELO AQP</span></div>
    </div>
    <div class="web">www.cargavelorumbo.pe</div>
  </header>

  <div class="hero" role="img" aria-label="Tractocamión blanco con semirremolque verde cargado de ladrillos en un patio de tierra">
  </div>

  <svg class="curve" width="849" height="1200" viewBox="0 0 849 1200" aria-hidden="true">
    <path d="M0,500 C260,430 560,470 849,600 L849,640 C560,505 260,470 0,540 Z" fill="#138a78"/>
    <path d="M0,528 C260,462 560,500 849,628 L849,1200 L0,1200 Z" fill="#ffffff"/>
  </svg>

  <div class="photo-disc disc-team" role="img" aria-label="Equipo de trabajo frente a la oficina de la empresa"><span></span></div>
  <div class="photo-disc disc-dump" role="img" aria-label="Volquete verde en operación de carga"><span></span></div>
  <div class="photo-disc disc-tipper" role="img" aria-label="Camión volquete blanco con tolva verde"><span></span></div>

  <section class="clientes">
    <h2 class="heading">CLIENTES</h2>
    <p class="copy">Nuestra mejor carta de presentación, es la satisfacción de nuestros clientes. Contamos con experiencia ofreciendo nuestros servicios de transporte de mercaderías en general, materiales y/o residuos peligrosos u otros por todo el sur del Perú, así como también en la ciudad de Lima;en importantes proyectos mineros como Cerro Alto, Los Pinos; alquilando unidades para el mantenimiento de carreteras en la provincia de Arequipa y Ayacucho; Transporte local de distribución de mercaderías en Arequipa, el llamado transporte capilar; entre otros.</p>
  </section>

  <section class="panel flota">
    <h2 class="heading">FLOTA</h2>
    <p class="copy">Es nuestra preocupación contar con unidades en excelente estado, que nos permitan realizar nuestras operaciones sin interrupciones por mantenimientos no planificados. Por tal motivo es que contamos una flota de unidades moderna. La cual describimos a continuación:</p>
  </section>

  <section class="panel servicios">
    <h2 class="heading">SERVICIOS</h2>
    <p class="copy">La “Superación” es uno de los valores pilares de nuestra organización. Es por eso que desde nuestra fundación a la fecha venimos incrementando la cantidad de servicios que brindamos, con el objetivo de adecuarnos a las necesidades de nuestros clientes. A la fecha los servicios que brindamos son:</p>
  </section>

  <section class="routes">
    <h2 class="heading routes-title">ROUTES</h2>
    <svg class="routes-lines" width="849" height="1200" viewBox="0 0 849 1200" aria-hidden="true" fill="none" stroke="#b5b5b5" stroke-width="1.5">
      <path d="M436,695.5H814M436,752.5H814M436,816.5H814M436,873.5H814M436,937.5H814M436,994.5H814M436,1059.5H814"/>
      <path d="M481,776V793M481,897V914M481,1018V1036M770,776V793M770,897V914"/>
      <path d="M481,1083V1092M529,1083V1092M577,1083V1092M626,1083V1092M674,1083V1092M722,1083V1092M770,1083V1088H722"/>
      <path d="M481,1088H577M626,1088H722"/>
    </svg>
    <div class="stop c1 r1">LIMA</div><div class="stop c2 r1">PISCO</div><div class="stop c3 r1">ICA</div><div class="stop c4 r1">NASCA</div>
    <div class="stop c1 r2">CHALA</div><div class="stop c2 r2">ATICO</div><div class="stop c3 r2">OCOÑA</div><div class="stop c4 r2">CAMANA</div>
    <div class="stop c1 r3">PEDREGAL</div><div class="stop c2 r3">MAJES</div><div class="stop c3 r3">MOLLENDO</div><div class="stop c4 r3">MATARANI</div>
    <div class="stop c1 r4">ILO</div><div class="stop c2 r4">MOQUEGUA</div><div class="stop c3 r4 tight">COCACHACRA</div><div class="stop c4 r4">TACNA</div>
    <div class="stop c1 r5">AREQUIPA</div><div class="stop c2 r5">JULIACA</div><div class="stop c3 r5">PUNO</div><div class="stop c4 r5">ILAVE</div>
    <div class="stop c1 r6 tight">DESAGUADERO</div><div class="stop c2 r6">CUSCO</div><div class="stop c3 r6">SICUANI</div><div class="stop c4 r6">CHIVAY</div>
    <div class="stop c1 r7">IMATA</div><div class="stop c2 r7">SANTA LUCIA</div><div class="stop c3 r7">AYAVIRI</div><div class="stop c4 r7">PUERTO<br>MALDONADO</div>
    <div class="stop b1 r8">MACUSANI</div><div class="stop b2 r8">MAZUCO</div><div class="stop b3 r8">ESPINAR</div>
  </section>

  <div class="footer-band"></div>
</div>
</body>
</html>
```